Design Simple & Basic Advertising Poster for Quivel and Dermal Filler

I need a few poster designs to display in a small salon, the services I wish to promote are Quivel and Dermal Filler. I am looking for something visually simple including a high quality picture, I have given an idea as to the type of image by attaching a few.

Text wise I would like to have some sort of prominent titling, something along the lines of "Quivel & Dermal Filler" and some text to say that it is available or is carried out at this salon. I am open two suggestions as to the text content but want it to be simple and to the point.

Please avoid anything pink, flowery or vivid colours. I am looking to keep it professional as it is a service at the upper end of cost for salons.

Please do not include any needles in the picture.

Impact is one of the key things I am looking for, something that strongly draws the eye.

```html
<!DOCTYPE html>
<html lang="en">
<head>
<meta charset="utf-8">
<title>Quivel &amp; Dermal Filler Posters</title>
<link rel="stylesheet" href="https://fonts.googleapis.com/css2?family=Archivo+Black&family=Oswald:wght@500;600;700&family=Montserrat:wght@400&family=Roboto+Condensed:wght@700;800&display=swap">
<style>
  :root {
    --stage-top: #e6e6e7;
    --stage-bottom: #d4d3d4;
    --paper: #f6f7f9;
    --paper-shade: #eceef2;
    --ink: #16131e;
    --ink-warm: #2a1d24;
    --plum: #4e1a38;
    --plum-dark: #3f1530;
    --mauve-band: #b59ba8;
    --white: #ffffff;
    --skin-light: rgba(236, 224, 220, 0.95);
    --skin-mid: rgba(214, 196, 190, 0.9);
    --hair: rgba(66, 52, 60, 0.85);
    --hair-soft: rgba(66, 52, 60, 0);
  }
  * { margin: 0; padding: 0; box-sizing: border-box; }
  html, body { width: 1200px; height: 958px; overflow: hidden; }
  body {
    position: relative;
    background: linear-gradient(180deg, var(--stage-top) 0%, var(--stage-bottom) 100%);
  }
  .poster {
    position: absolute;
    overflow: hidden;
    background: linear-gradient(160deg, var(--white) 0%, var(--paper) 55%, var(--paper-shade) 100%);
  }

  /* Poster: Discover */
  .poster--discover { left: 23px; top: 22px; width: 490px; height: 693px; }
  .poster--discover .portrait {
    position: absolute; left: 0; top: 0; width: 340px; height: 693px;
    background:
      radial-gradient(ellipse 150px 120px at 40px 20px, var(--hair) 0%, var(--hair-soft) 100%),
      radial-gradient(ellipse 200px 300px at 70px 300px, var(--skin-mid) 0%, rgba(214,196,190,0.35) 70%, rgba(214,196,190,0) 100%),
      radial-gradient(ellipse 260px 90px at 100px 693px, var(--skin-mid) 0%, rgba(214,196,190,0) 100%);
  }
  .discover-copy {
    position: absolute; right: 24px; top: 381px;
    text-align: right; color: var(--ink);
  }
  .discover-copy .tag {
    display: inline-block; background: var(--plum); color: var(--white);
    font-family: "Roboto Condensed", sans-serif; font-weight: 800;
    font-size: 22px; line-height: 27px; padding: 0 6px; letter-spacing: 0.2px;
  }
  .discover-copy .lead {
    font-family: "Roboto Condensed", sans-serif; font-weight: 800;
    font-size: 22px; line-height: 26px; color: var(--plum); margin-top: 2px;
  }
  .discover-copy .service {
    font-family: "Archivo Black", sans-serif; font-size: 40px; line-height: 46px;
    letter-spacing: -0.5px;
  }
  .discover-copy .amp { line-height: 44px; }

  /* Poster: Complete service */
  .poster--service { left: 537px; top: 25px; width: 646px; height: 912px; }
  .poster--service .portrait {
    position: absolute; left: 0; top: 280px; width: 420px; height: 632px;
    background:
      radial-gradient(ellipse 330px 150px at 120px 30px, var(--hair) 0%, var(--hair-soft) 100%),
      radial-gradient(ellipse 300px 420px at 130px 400px, var(--skin-mid) 0%, rgba(214,196,190,0.4) 65%, rgba(214,196,190,0) 100%);
  }
  .service-heading {
    position: absolute; left: 0; top: 37px; width: 616px;
    text-align: center; color: var(--ink-warm);
  }
  .service-heading .kicker {
    font-family: "Montserrat", sans-serif; font-weight: 400;
    font-size: 30px; line-height: 34px; letter-spacing: 9px; padding-left: 9px;
  }
  .service-heading .title {
    font-family: "Oswald", sans-serif; font-weight: 700;
    font-size: 88px; line-height: 80px; margin-top: 0; transform: scaleX(0.85);
  }
  .service-heading .joiner {
    font-family: "Oswald", sans-serif; font-weight: 600;
    font-size: 34px; line-height: 44px;
  }
  .name-band {
    position: absolute; left: 120px; top: 201px; width: 404px; height: 148px;
    background: var(--mauve-band);
    display: flex; align-items: center; justify-content: center;
  }
  .name-band .name {
    font-family: "Oswald", sans-serif; font-weight: 700; color: var(--white);
    font-size: 108px; line-height: 1; letter-spacing: 1px;
  }
  .service-sub {
    position: absolute; left: 340px; top: 356px; width: 292px;
    text-align: center; color: var(--plum-dark);
    font-family: "Oswald", sans-serif; font-weight: 700;
    font-size: 58px; line-height: 58px; letter-spacing: 1px;
  }
</style>
</head>
<body>
  <section class="poster poster--discover">
    <div class="portrait" role="img" aria-label="Studio portrait of a woman with dark eye makeup and plum lipstick, half of her face at the left edge"></div>
    <div class="discover-copy">
      <div class="tag">DISCOVER</div>
      <div class="lead">OUR SPECIAL</div>
      <div class="service">Quivel</div>
      <div class="service amp">&amp;</div>
      <div class="service">Dermal Filler</div>
    </div>
  </section>

  <section class="poster poster--service">
    <div class="portrait" role="img" aria-label="Close-up portrait of a woman with slicked-back dark hair and smoky eye makeup"></div>
    <div class="service-heading">
      <div class="kicker">COMPLETE</div>
      <div class="title">SERVICE</div>
      <div class="joiner">FOR</div>
    </div>
    <div class="name-band"><span class="name">QUIVEL</span></div>
    <div class="service-sub">&amp; DERMAL<br>FILLER</div>
  </section>
</body>
</html>
```